Web Page needed for Dr. Wanbrook Consult

The company works in the consultant business for processes in large projects our of engineering and construction business. We develop strategies but work also in critical projects to get them right.
The page should have a modern appearance but though a classy and luxury touch.
Updates

The project was bought in a package, logo plus web page. Now the designers do submit logos again, although the logo has been set. This part is only the web site. I changed the text to clarify it, I contacted support to put that right, but that needs an extension of minimum 7 days to catch up.

Due to the confusion in the project, it was first set up as logo project and later corrected (I have no clue how that happened, as I bought a package with logo + web, and logo is already done), there is a large delay in getting feedback. Please be so kind and extend until 31.01. In Europe there is holidays until 07.01. and I have no time to discuss the topics with my client until 10.01., than we need to feed in response and get changes done.

Logo Text

The logo is already fixed, I asked for web page.

Number of Pages Required

5+ page

Font styles to use
Sans Serif

Colors

Designer to choose colors to be used in the design.

Requirements
Must have
• Home/Start
• Lean Construction
• Lean Equipment
• Lean Design
• Lean Training
• Team
• Contact
• Imprint
Nice to have
• Darker color, luxury appearance, please integrate the logo in the attachment here.
• I would like to have a web page with animated context, such as this one here: https://tovalmerworks.example

```html
<!DOCTYPE html>
<html lang="en">
<head>
<meta charset="utf-8">
<title>Dr. Wanbrook Consult</title>
<link rel="stylesheet" href="https://fonts.googleapis.com/css2?family=Anton&family=Marcellus&family=Quicksand:wght@400;500;600&display=swap">
<style>
:root{
  --green:#8fc13e;
  --green-soft:#9ccb4a;
  --blue:#2f6eb5;
  --blue-dark:#245a96;
  --ink:#333;
  --muted:#666;
  --dark:#2a3125;
  --white:#fff;
}
*{box-sizing:border-box;margin:0;padding:0}
html,body{width:1200px;height:4078px;overflow:hidden}
body{font-family:"Quicksand",sans-serif;color:var(--ink);background:var(--white);position:relative}
.serif{font-family:"Marcellus",serif}
.btn{position:absolute;background:var(--blue);color:var(--white);font-family:"Marcellus",serif;font-size:16px;display:flex;align-items:center;justify-content:center;border-radius:5px;letter-spacing:.5px;text-decoration:none}

/* header */
.site-header{position:absolute;top:0;left:0;width:1200px;height:88px}
.brand{position:absolute;left:76px;top:26px;display:flex;align-items:center;gap:10px;font-family:"Marcellus",serif;font-size:24px;color:var(--blue)}
.brand-dot{width:16px;height:16px;background:var(--green);border-radius:50%}
.main-nav{position:absolute;top:36px;left:0;width:1200px;font-size:15px;font-weight:500}
.main-nav a{position:absolute;color:var(--ink);text-decoration:none}
.main-nav a.active{color:var(--green)}
.nav-underline{position:absolute;left:458px;top:83px;width:64px;height:4px;background:var(--green)}

/* hero */
.hero{position:absolute;top:88px;left:0;width:1200px;height:590px;background:var(--green)}
.hero-photo{position:absolute;inset:0;border-radius:0 240px 240px 0;
  background:
    linear-gradient(90deg,rgba(30,30,24,.55) 0%,rgba(30,30,24,.25) 40%,rgba(30,30,24,0) 60%),
    radial-gradient(ellipse 90px 60px at 440px 70px,rgba(230,170,40,.85),rgba(230,170,40,0)),
    radial-gradient(ellipse 80px 55px at 830px 60px,rgba(40,110,130,.8),rgba(40,110,130,0)),
    radial-gradient(ellipse 70px 50px at 95px 75px,rgba(220,220,215,.6),rgba(220,220,215,0)),
    radial-gradient(ellipse 200px 260px at 520px 420px,rgba(190,200,70,.75),rgba(190,200,70,0)),
    radial-gradient(ellipse 190px 240px at 900px 400px,rgba(160,205,60,.8),rgba(160,205,60,0)),
    radial-gradient(ellipse 160px 200px at 100px 420px,rgba(150,170,60,.55),rgba(150,170,60,0)),
    radial-gradient(ellipse 220px 140px at 1000px 120px,rgba(210,190,140,.55),rgba(210,190,140,0)),
    radial-gradient(ellipse 120px 120px at 260px 180px,rgba(170,100,40,.5),rgba(170,100,40,0)),
    linear-gradient(100deg,#2f2e24 0%,#4a4836 40%,#55573a 70%,#3f4a2c 100%)}
.hero-title{position:absolute;left:81px;top:214px;font-family:"Anton",sans-serif;font-weight:400;font-size:45px;line-height:48px;color:var(--white);letter-spacing:.5px}
.hero-text{position:absolute;left:78px;top:325px;width:420px;font-size:17px;line-height:27px;color:var(--white)}

/* welcome */
.welcome{position:absolute;top:677px;left:0;width:1200px;height:375px;background:var(--green);color:var(--white);text-align:center}
.welcome-kicker{position:absolute;top:62px;width:100%;font-size:21px}
.welcome-title{position:absolute;top:92px;width:100%;font-size:44px;font-weight:400}
.welcome p{position:absolute;left:305px;width:590px;font-size:13.5px;line-height:27px}
.scroll-cue{position:absolute;left:569px;top:1021px;width:62px;height:62px;border-radius:50%;background:var(--blue);border:5px solid var(--white)}

/* services */
.section-title{position:absolute;width:1200px;text-align:center;font-family:"Marcellus",serif;font-size:44px;font-weight:400;color:var(--blue)}
.service{position:absolute;width:397px;height:364px;display:flex;align-items:center;justify-content:center;font-family:"Marcellus",serif;font-size:29px;color:var(--white)}
.service-construction{left:193px;top:1228px;background:linear-gradient(160deg,#4f8bcb,#3a76b8)}
.service-equipment{left:611px;top:1228px;background:linear-gradient(160deg,#5a4432,#2e2a24)}
.service-design{left:193px;top:1613px;background:linear-gradient(160deg,#9a7a86,#d8d2cc)}
.service-training{left:611px;top:1613px;background:linear-gradient(180deg,#2d4a7c,#6e7a5a)}

/* call to action */
.cta-band{position:absolute;left:103px;top:2135px;width:1097px;height:365px;border-radius:182px 0 0 182px;background:linear-gradient(90deg,var(--green),#a4cf4f)}
.cta-person{position:absolute;left:245px;top:2031px;width:293px;height:469px;border-radius:140px 140px 0 0;background:linear-gradient(180deg,#e3b52a 0%,#6d86a8 40%,#3d5a88 100%)}
.cta-brand{position:absolute;left:681px;top:2220px;font-family:"Quicksand",sans-serif;font-weight:500;font-size:20px;color:var(--white)}
.cta-text{position:absolute;left:681px;top:2288px;font-size:24px;line-height:34px;color:var(--white);font-weight:500}

/* team */
.team-intro{position:absolute;top:2617px;width:1200px;text-align:center;font-size:14px;line-height:28px;color:var(--muted)}
.member{position:absolute;top:2711px;width:200px;text-align:center}
.avatar{width:124px;height:124px;border-radius:50%;margin:0 auto;background:radial-gradient(circle at 50% 40%,#d9c6b6,#c7cbbd)}
.member-name{font-family:"Marcellus",serif;font-size:20px;color:var(--blue);margin-top:38px}
.member-role{font-size:14px;color:var(--muted);margin-top:4px}
.socials{display:flex;justify-content:center;gap:7px;margin-top:14px}
.socials span{width:36px;height:36px;border-radius:50%;border:1.5px solid #ccc}
.socials span.on{background:var(--blue);border-color:var(--blue)}

/* contact */
.contact-wrap{position:absolute;top:3036px;left:0;width:1200px;height:557px;background:linear-gradient(var(--white) 50%,var(--dark) 50%)}
.contact{position:absolute;inset:0;border-radius:0 220px 220px 0;background:linear-gradient(180deg,#9bca45,#8fba3e 70%,#7d9a3a)}
.contact-title{position:absolute;top:62px;width:100%;text-align:center;font-family:"Marcellus",serif;font-size:42px;font-weight:400;color:var(--white)}
.contact-intro{position:absolute;top:117px;width:100%;text-align:center;font-size:14px;line-height:27px;color:var(--white);font-weight:500}
.field{position:absolute;background:var(--white);font-size:13px;color:#777;padding:18px 16px}
.submit{left:532px;top:439px;width:134px;height:50px;font-size:18px}

/* footer */
.site-footer{position:absolute;top:3593px;left:0;width:1200px;height:485px;background:linear-gradient(180deg,#2d3327,#22281f)}
.footer-brand{position:absolute;top:90px;width:100%;text-align:center;font-family:"Marcellus",serif;font-size:26px;color:var(--green)}
.contact-strip{position:absolute;left:193px;top:181px;width:814px;height:82px;border:1px solid rgba(255,255,255,.45);display:flex}
.contact-item{position:relative;height:100%;display:flex;align-items:center;gap:16px;padding-left:30px;color:var(--white)}
.contact-item + .contact-item{border-left:1px solid rgba(255,255,255,.45)}
.contact-item b{display:block;font-family:"Marcellus",serif;font-weight:400;font-size:17px}
.contact-item small{font-size:13px}
.footer-social{position:absolute;top:309px;left:530px;display:flex;gap:12px}
.footer-social span{width:38px;height:38px;border-radius:50%;background:var(--blue)}
.footer-nav{position:absolute;top:376px;width:100%;text-align:center;font-size:14px;color:var(--white)}
.copyright{position:absolute;top:406px;width:100%;text-align:center;font-size:14px;color:var(--white)}
.copyright em{font-style:normal;color:var(--green)}
</style>
</head>
<body>

<header class="site-header">
  <div class="brand"><span class="brand-dot"></span>Dr. Wanbrook Consult</div>
  <nav class="main-nav">
    <a class="active" style="left:467px">Home</a>
    <a style="left:539px">Construction</a>
    <a style="left:656px">Equipment</a>
    <a style="left:761px">Design</a>
    <a style="left:840px">Traning</a>
    <a style="left:922px">Team</a>
    <a style="left:987px">Contact</a>
    <a style="left:1068px">imprint</a>
  </nav>
  <div class="nav-underline"></div>
</header>

<section class="hero">
  <div class="hero-photo" role="img" aria-label="Smiling engineers in yellow hard hats and green safety vests on a construction site"></div>
  <h1 class="hero-title">Engineering And<br>Construction Business</h1>
  <p class="hero-text">We develop strategies but work also in critical projects to get them right.</p>
  <a class="btn" style="left:78px;top:400px;width:164px;height:50px">CONTACT US</a>
</section>

<section class="welcome">
  <div class="welcome-kicker serif">Welcome To</div>
  <h2 class="welcome-title serif">Dr. Wanbrook Consult</h2>
  <p style="top:157px">Lorem Ipsum is simply dummy text of the printing and typesetting industry. Lorem Ipsum has been the industry's standard dummy.</p>
  <p style="top:226px">Lorem Ipsum is simply dummy text of the printing and typesetting industry. Lorem Ipsum has been the industry's standard dummy text ever since the Lorem Ipsum is simply dummy text of the printing.</p>
</section>
<div class="scroll-cue">
  <svg width="52" height="52" viewBox="0 0 52 52"><path d="M16 21l10 8 10-8M16 28l10 8 10-8" fill="none" stroke="#fff" stroke-width="2"/></svg>
</div>

<h2 class="section-title" style="top:1130px">What We Do</h2>
<div class="service service-construction" role="img" aria-label="Workers reviewing plans in front of a steel frame building">Lean Construction</div>
<div class="service service-equipment" role="img" aria-label="Aerial view of workers on a construction floor">Lean Equipment</div>
<div class="service service-design" role="img" aria-label="Hands drawing on a technical plan">Lean Design</div>
<div class="service service-training" role="img" aria-label="Workers looking up at cranes and high-rise buildings">Lean Training</div>

<div class="cta-band" role="img" aria-label="Construction site with cranes in green tint"></div>
<div class="cta-person" role="img" aria-label="Smiling worker in hard hat holding a tablet"></div>
<div class="cta-brand">Dr. Wanbrook Consult</div>
<p class="cta-text">If You Have an Any Question For<br>Contact Us Today!</p>
<a class="btn" style="left:681px;top:2370px;width:166px;height:50px">CONTACT US</a>

<h2 class="section-title" style="top:2555px">Meet Our Team</h2>
<p class="team-intro">Lorem Ipsum is simply dummy text of the printing and typesetting industry.<br>Lorem Ipsum has been the industry's standard</p>
<div class="member" style="left:95px"><div class="avatar" role="img" aria-label="Team member portrait"></div><div class="member-name">Member Name</div><div class="member-role">Lorem Ipsum text</div><div class="socials"><span class="on"></span><span></span><span></span></div></div>
<div class="member" style="left:363px"><div class="avatar" role="img" aria-label="Team member portrait"></div><div class="member-name">Member Name</div><div class="member-role">Lorem Ipsum text</div><div class="socials"><span class="on"></span><span></span><span></span></div></div>
<div class="member" style="left:632px"><div class="avatar" role="img" aria-label="Team member portrait"></div><div class="member-name">Member Name</div><div class="member-role">Lorem Ipsum text</div><div class="socials"><span class="on"></span><span></span><span></span></div></div>
<div class="member" style="left:903px"><div class="avatar" role="img" aria-label="Team member portrait"></div><div class="member-name">Member Name</div><div class="member-role">Lorem Ipsum text</div><div class="socials"><span class="on"></span><span></span><span></span></div></div>

<section class="contact-wrap">
  <div class="contact" role="img" aria-label="Faded construction site behind green overlay"></div>
  <h2 class="contact-title">Contact Us</h2>
  <p class="contact-intro">Lorem Ipsum is simply dummy text of the printing and typesetting industry.<br>Lorem Ipsum has been the industry's standard</p>
  <div class="field" style="left:269px;top:198px;width:312px;height:51px">Name *</div>
  <div class="field" style="left:592px;top:198px;width:312px;height:51px">Email *</div>
  <div class="field" style="left:269px;top:261px;width:312px;height:51px">Phone *</div>
  <div class="field" style="left:592px;top:261px;width:312px;height:51px">Services *</div>
  <div class="field" style="left:269px;top:323px;width:635px;height:103px">Message *</div>
  <a class="btn submit">SUBMIT</a>
</section>

<footer class="site-footer">
  <div class="footer-brand">Dr. Wanbrook Consult</div>
  <div class="contact-strip">
    <div class="contact-item" style="width:263px">
      <svg width="26" height="42" viewBox="0 0 26 42"><rect x="2" y="2" width="22" height="38" rx="4" fill="none" stroke="#8fc13e" stroke-width="2"/><line x1="9" y1="34" x2="17" y2="34" stroke="#8fc13e" stroke-width="2"/></svg>
      <div><b>Phone</b><small>-123 456 7890</small></div>
    </div>
    <div class="contact-item" style="width:279px">
      <svg width="44" height="46" viewBox="0 0 44 46"><path d="M22 4a9 9 0 0 1 9 9c0 7-9 16-9 16s-9-9-9-16a9 9 0 0 1 9-9z" fill="none" stroke="#8fc13e" stroke-width="2"/><circle cx="22" cy="13" r="3" fill="none" stroke="#8fc13e" stroke-width="2"/><path d="M2 44l6-16 8 3M42 44l-6-16-8 3M2 44h40" fill="none" stroke="#8fc13e" stroke-width="2"/></svg>
      <div><b>Location</b><small>101 - Lorem ipsum simple</small></div>
    </div>
    <div class="contact-item" style="width:270px">
      <svg width="44" height="30" viewBox="0 0 44 30"><rect x="1" y="1" width="42" height="28" fill="none" stroke="#8fc13e" stroke-width="2"/><path d="M1 1l21 16L43 1M1 29l15-14M43 29L28 15" fill="none" stroke="#8fc13e" stroke-width="2"/></svg>
      <div><b>Email</b><small>info@wanbrook.example</small></div>
    </div>
  </div>
  <div class="footer-social"><span></span><span></span><span></span></div>
  <div class="footer-nav">Home &nbsp;|&nbsp; Construction &nbsp;|&nbsp; Equipment &nbsp;|&nbsp; Design &nbsp;|&nbsp; Traning &nbsp;|&nbsp; Team &nbsp;|&nbsp; Contact</div>
  <div class="copyright">© <em>Dr. Wanbrook Consult</em> – 2020 All Rights reserved</div>
</footer>

</body>
</html>
```